Flyer Design Project

We need a flyer for a monthly event that we will be having. The flyer needs to be editable in either adobe illustrator or photoshop so that we can change the details such as the date if needed... Preferable in vector art.

Name of Event : Sandalmania

Price of Tickets: $15 Tickets- Entry fee ensures a pair of thongs upon leaving, drink specials all night and priority entry.

WHEN- FEB 20th
WHERE- Velvet Loft
DJ: Tessa Harlow
web: www.velvetloftbar.com.au
ph: 9146 3705

Drink specials from 7-9pm
$3 Pots
$4 basics
$4 kelvanos

$1 pizza from 8pm-10pm

FREE PAIR OF THONGS ON DEPARTURE

Drink specials continue throughout the night

Open 7pm-3am
Updates

Hi there,

Just to be clear, a pair of thongs isĀ referringĀ to flip flops or sandals (not underwear)... thanks

Target Market(s)

University Students 18-24 years old

Industry/Entity Type

Apartment

Requirements
Must have
• must have our logo

```html
<!DOCTYPE html>
<html lang="en">
<head>
<meta charset="utf-8">
<title>Sandalmania – Feb 20th at Velvet Loft</title>
<link rel="stylesheet" href="https://fonts.googleapis.com/css2?family=Bowlby+One+SC&family=Itim&display=swap">
<style>
  :root {
    --sand-light: #dcc29b;
    --sand-mid: #cfae80;
    --sand-dark: #b08556;
    --foam: #e4e3dc;
    --water-light: #7d95a8;
    --water-dark: #2f4763;
    --thong-yellow: #e6c228;
    --thong-shade: #c9a514;
    --cap-red: #9c1b22;
    --title-red: #9a2a1c;
    --title-edge: #2c3f8c;
    --engrave: #8b6a43;
    --ink: #111111;
    --white: #ffffff;
    --accent-yellow: #f2d21c;
    --time-red: #8e1a12;
  }
  * { margin: 0; padding: 0; box-sizing: border-box; }
  html, body { width: 848px; height: 1200px; overflow: hidden; background: #ffffff; }
  .flyer {
    position: relative;
    width: 848px;
    height: 1200px;
    overflow: hidden;
    font-family: "Itim", "Trebuchet MS", sans-serif;
    background: var(--sand-light);
  }
  .flyer__scene, .flyer__sandals { position: absolute; left: 0; top: 0; }
  .price-badge {
    position: absolute; left: 72px; top: 52px; width: 92px; height: 92px;
    border-radius: 50%; background: var(--cap-red);
    box-shadow: 0 3px 6px rgba(0,0,0,.35);
    display: flex; align-items: center; justify-content: center;
    color: var(--accent-yellow); font-size: 40px; line-height: 1;
  }
  .event-date, .event-dj {
    position: absolute; right: 40px; color: var(--engrave);
    text-shadow: 1px 1px 0 rgba(255,255,255,.35), -1px -1px 0 rgba(0,0,0,.15);
  }
  .event-date { top: 26px; right: 50px; font-size: 54px; transform: rotate(4deg); }
  .event-dj { top: 100px; right: 30px; font-size: 36px; transform: rotate(4deg); }
  .event-title {
    position: absolute; left: 0; width: 848px; top: 602px; text-align: center;
    font-family: "Bowlby One SC", "Arial Black", sans-serif;
    font-size: 78px; line-height: 1; letter-spacing: 3px;
    color: var(--title-red);
    text-shadow: 2px 2px 0 var(--title-edge), 4px 4px 0 var(--title-edge);
  }
  .event-hours {
    position: absolute; left: 664px; top: 678px;
    color: var(--time-red); font-size: 20px; font-weight: 700;
  }
  .pizza-time { position: absolute; left: 106px; top: 782px; font-size: 22px; color: var(--ink); }
  .pizza-deal { position: absolute; left: 50px; top: 812px; font-size: 27px; color: var(--ink); font-weight: 700; }
  .section-heading { font-size: 29px; color: var(--ink); font-weight: 700; }
  .ticket-perks { position: absolute; left: 50px; top: 898px; }
  .ticket-perks ul { list-style: none; margin-top: 8px; padding-left: 14px; }
  .ticket-perks li { color: var(--white); font-size: 29px; line-height: 40px; }
  .drink-specials { position: absolute; left: 576px; top: 848px; }
  .drink-specials__time {
    position: absolute; left: -42px; top: 48px; font-size: 24px; color: var(--ink); white-space: nowrap;
  }
  .drink-specials ul { list-style: none; position: absolute; left: 86px; top: 40px; text-align: left; }
  .drink-specials li { color: var(--white); font-size: 29px; line-height: 44px; white-space: nowrap; }
  .venue-name {
    position: absolute; left: 32px; top: 1080px;
    color: var(--accent-yellow); font-size: 52px; line-height: 1;
    display: flex; align-items: center; gap: 14px;
  }
  .venue-name__dot { width: 16px; height: 16px; border-radius: 50%; background: var(--accent-yellow); }
  .venue-contact { position: absolute; left: 444px; top: 1084px; color: var(--accent-yellow); font-size: 25px; line-height: 34px; }
</style>
</head>
<body>
<main class="flyer">
  <svg class="flyer__scene" width="848" height="1200" viewBox="0 0 848 1200" role="img" aria-label="Beach backdrop: sand fading into foam and sea water">
    <defs>
      <linearGradient id="sandTop" x1="0" y1="0" x2="0" y2="1">
        <stop offset="0" stop-color="#e0c8a2"/>
        <stop offset="1" stop-color="#d2b284"/>
      </linearGradient>
      <linearGradient id="sandBand" x1="0" y1="0" x2="0" y2="1">
        <stop offset="0" stop-color="#b68a5a"/>
        <stop offset="1" stop-color="#caa577"/>
      </linearGradient>
      <linearGradient id="sea" x1="0" y1="0" x2="0" y2="1">
        <stop offset="0" stop-color="#8ea4b4"/>
        <stop offset=".35" stop-color="#5f7c98"/>
        <stop offset="1" stop-color="#2b405c"/>
      </linearGradient>
    </defs>
    <rect width="848" height="1200" fill="url(#sandTop)"/>
    <path d="M0 470 C140 430 260 480 420 470 C580 460 700 420 848 440 L848 1200 L0 1200 Z" fill="url(#sandBand)"/>
    <path d="M0 520 C160 500 300 530 450 525 C620 520 740 500 848 505 L848 1200 L0 1200 Z" fill="#c7a273" opacity=".6"/>
    <path d="M0 700 C90 680 200 690 300 720 C420 760 560 700 700 660 C770 640 820 640 848 650 L848 1200 L0 1200 Z" fill="var(--foam)"/>
    <path d="M0 840 C140 815 300 830 420 828 C560 825 700 800 848 790 L848 1200 L0 1200 Z" fill="url(#sea)"/>
  </svg>

  <svg class="flyer__sandals" width="848" height="1200" viewBox="0 0 848 1200" role="img" aria-label="Illustration of a pair of yellow flip-flop sandals standing in the sand at the water's edge">
    <defs>
      <linearGradient id="sandalFill" x1="0" y1="0" x2="1" y2="1">
        <stop offset="0" stop-color="var(--thong-yellow)"/>
        <stop offset="1" stop-color="var(--thong-shade)"/>
      </linearGradient>
    </defs>
    <rect x="140" y="180" width="270" height="660" rx="120" fill="url(#sandalFill)"/>
    <rect x="428" y="180" width="278" height="660" rx="120" fill="url(#sandalFill)"/>
  </svg>

  <div class="price-badge">$15</div>
  <p class="event-date">Feb 20th</p>
  <p class="event-dj">DJ Tessa Harlow</p>

  <h1 class="event-title">Sandalmania</h1>
  <p class="event-hours">7pm to 3am</p>

  <p class="pizza-time">8 to 10pm</p>
  <p class="pizza-deal">$1 pizza</p>

  <section class="ticket-perks">
    <h2 class="section-heading">Tickets include</h2>
    <ul>
      <li>Priority entry</li>
      <li>Drinks specials all night</li>
      <li>Pair of thongs upon leaving</li>
    </ul>
  </section>

  <section class="drink-specials">
    <h2 class="section-heading">Drink specials</h2>
    <p class="drink-specials__time">7 to 9pm</p>
    <ul>
      <li>$3 Pots</li>
      <li>$4 Basics</li>
      <li>$4 Kelvanos</li>
    </ul>
  </section>

  <div class="venue-name"><span>Velvet Loft</span><span class="venue-name__dot"></span></div>
  <address class="venue-contact" style="font-style:normal">
    Ph: 9146 3705<br>
    Address: 41 Marlow Street Eastbay<br>
    www.velvetloftbar.com.au
  </address>
</main>
</body>
</html>
```